INTERNATIONAL SPEAKING BUSINESS FOR WOMEN NEEDS A BROCHURE DESIGN

HEARTWARD CIRCLE IS AN INTERNATIONAL FEMALE NETWORK PROVIDING ITS MEMBERS THE UK'S NUMBER ONE RELATIONSHIP SEMINAR FOR WOMEN.
WE ARE ABOUT TO GO LIVE AGAIN AFTER 18 MONTHS AND ONE OF OUR OFFERINGS AT THIS LIVE EVENT, IS OUR CONNECTION GROWTH PROGRAMME - AND THIS IS WHERE YOU COME IN :)
IM LOOKING FOR AN ELEGANT, EASY AND WARM TO THE EYE BROCHURE WHICH CAPTURES SOME OF OUR BEST TESTIMONIALS AND CLIENTS. WE HAVE THE LOGO, THE IMAGES AND THE COPY . WE JUST NEED YOUR AMAZING CREATIVE TALENT AND SKILL TO PUT IT ALL TOGETHER TO LOOK ELEGANT AND PROFESSIONAL, YET WELCOMING AND INSPIRING.
OUR IDEAL CLIENT IS A SINGLE, SUCCESSFUL, PROFESSIONAL WOMAN WANTING TO FIND A SOLUTION TO HER RELATIONSHIP CHALLENGES. SHE WANTS TO LET GO OF HER FEARS OF PAST RELATIONSHIPS AND ALIGN WITH AN AMAZING RELATIONSHIP. OUR AIM WITH THE BROCHURE IS TO SHOW THEM WHAT WE DO, HOW WE DO IT AND HOW OUR EXISTING CLIENTS HAVE ALREADY DONE THIS.
THIS IS JUST ONE OF MANY CREATIVE WORKS NEEDED TO BE CARRIED OUT OVER THESE NEXT FEW WEEKS
SO WE ARE LOOKING FOR OUR IDEAL CREATIVE PARTNER ! HOPING TO FIND YOU HERE ;)
heartwardcircle-example.com
professional, successful women between 30 and 65 looking to resolve their relationship problems
Speaking Business/ Seminars / webinars/ Relationships Coaching for Women
- Similar to logo and website heartwardcircle-example.com

```html
<!DOCTYPE html>
<html lang="en">
<head>
<meta charset="utf-8">
<title>Heartward Circle – Connection Growth Programme Brochure</title>
<link href="https://fonts.googleapis.com/css2?family=Montserrat:ital,wght@0,300;0,400;0,700;1,300;1,400&family=Oswald:wght@300;400;500&family=Roboto+Condensed:wght@300;400;700&display=swap" rel="stylesheet">
<style>
:root{
  --backdrop:#d4b89c;
  --paper:#ecebe8;
  --paper-fold:#e2e1de;
  --ink:#1d1d1d;
  --ink-soft:#3c3c3c;
  --grey:#7a7a7a;
  --ring:#4b4b4b;
  --pink:#cf3358;
  --blue:#1f4fa3;
  --navy:#1d3f8f;
  --black:#121212;
  --gold:#d9a93a;
}
*{box-sizing:border-box;margin:0;padding:0}
html,body{width:1200px;height:801px;overflow:hidden;background:var(--backdrop)}
.canvas{position:relative;width:1200px;height:801px}
.spread{position:absolute;top:185px;width:560px;height:431px;background:var(--paper);overflow:hidden;
  font-family:"Roboto Condensed",sans-serif;color:var(--ink)}
.spread--inside{left:25px}
.spread--outside{left:615px}
.fold-shade{position:absolute;top:0;bottom:0;left:280px;right:0;background:var(--paper-fold)}
.frame-line{position:absolute;border:0.6px solid #c9c8c4}

/* inside: about band */
.about-band{position:absolute;left:0;top:0;width:560px;height:97px;background:var(--black)}
.about-title{position:absolute;left:34px;top:13px;font:italic 300 10.5px "Montserrat",sans-serif;color:var(--pink);letter-spacing:.2px}
.about-copy{position:absolute;top:29px;font:italic 300 5.3px/1.4 "Montserrat",sans-serif;color:#f1f1f1}
.about-copy--a{left:34px;width:200px}
.about-copy--b{left:292px;width:146px}
.founder-photo{position:absolute;left:440px;top:8px;width:120px;height:89px;
  background:linear-gradient(135deg,#6a5a4c,#b58a6a 55%,#3a2d26);clip-path:polygon(14% 0,100% 0,100% 100%,52% 100%)}
.founder-stripe{position:absolute;left:440px;top:8px;width:120px;height:89px;background:var(--pink);
  clip-path:polygon(0 0,14% 0,52% 100%,40% 100%)}
.team-title{position:absolute;left:48px;top:104px;font:italic 300 10.5px "Montserrat",sans-serif;color:var(--ink)}
.team-slash{position:absolute;left:27px;top:106px;width:26px;height:11px;background:var(--pink);clip-path:polygon(0 0,70% 0,100% 100%,30% 100%)}
.fold-slash{position:absolute;left:492px;top:97px;width:20px;height:22px;background:#c9c8c4;clip-path:polygon(0 0,30% 0,100% 100%)}

.portrait{position:absolute;width:72px;height:72px;border-radius:50%;border:6px solid var(--ring)}
.tone-a{background:radial-gradient(circle at 50% 45%,#e7c39e,#b07d52 70%)}
.tone-b{background:radial-gradient(circle at 50% 45%,#e9d8b8,#9aa3a6 70%)}
.tone-c{background:radial-gradient(circle at 50% 45%,#d8b09a,#6b7a70 70%)}
.tone-d{background:radial-gradient(circle at 50% 45%,#d9b8a4,#8a8077 70%)}
.tone-e{background:radial-gradient(circle at 50% 45%,#d2a892,#4d4d4d 70%)}
.tone-f{background:radial-gradient(circle at 50% 45%,#c89278,#3b2a2c 70%)}

.quote{position:absolute;width:168px}
.quote--right{text-align:right}
.quote-name{font:700 6.3px "Roboto Condensed",sans-serif;color:var(--ink)}
.quote-role{font:300 6px "Montserrat",sans-serif;text-transform:uppercase;color:var(--ink-soft);margin-bottom:1px;letter-spacing:-.1px}
.quote-body{font:400 4.8px/1.5 "Roboto Condensed",sans-serif;color:var(--ink-soft)}

.foot-stripes{position:absolute;bottom:0;height:4px;display:flex}
.foot-stripes span{display:block;height:100%;transform:skewX(-40deg)}

/* outside: back cover */
.kicker{position:absolute;left:15px;top:16px;font:700 4.6px "Montserrat",sans-serif;letter-spacing:2px;color:var(--pink)}
.register-band{position:absolute;left:0;top:30px;width:185px;height:46px;background:var(--black);
  clip-path:polygon(0 0,88% 0,100% 100%,0 100%);color:#fff;font:400 7.2px/1.35 "Montserrat",sans-serif;padding:12px 0 0 16px}
.stage-photo{position:absolute;left:196px;top:0;width:84px;height:133px;
  background:linear-gradient(160deg,#8fa6c6,#2e49a0 45%,#1a1f3a);clip-path:polygon(0 0,100% 0,100% 100%,38% 100%,0 30%)}
.stage-stripe{position:absolute;left:160px;top:38px;width:70px;height:95px;background:var(--pink);clip-path:polygon(0 0,22% 0,100% 100%,80% 100%)}
.sub-label{position:absolute;left:22px;top:84px;font:700 7.5px "Montserrat",sans-serif}
.sub-price{position:absolute;left:20px;top:93px;font:300 14px "Montserrat",sans-serif;color:var(--pink)}
.sub-copy{position:absolute;left:18px;top:119px;width:200px;font:400 6.3px/1.4 "Roboto Condensed",sans-serif}
.sub-copy b{font-weight:700}
.sub-note{position:absolute;left:18px;top:157px;width:160px;font:300 5px/1.4 "Roboto Condensed",sans-serif;color:var(--grey)}
.detail{position:absolute;left:22px;width:150px;font:400 4.6px/1.35 "Roboto Condensed",sans-serif;color:var(--pink)}
.detail h4{font:700 5.2px "Montserrat",sans-serif;color:var(--ink)}
.detail::before{content:"";position:absolute;left:-9px;top:1px;border-left:5px solid var(--pink);border-top:3px solid transparent;border-bottom:3px solid transparent}
.pink-block{position:absolute;left:142px;top:187px;width:82px;height:74px;background:var(--pink);clip-path:polygon(0 0,40% 0,100% 100%,60% 100%)}
.schedule{position:absolute;left:208px;top:200px;font:700 5px "Montserrat",sans-serif}
.schedule span{display:block;font:300 9px "Montserrat",sans-serif;color:var(--ink-soft);margin-top:1px}
.schedule-bracket{position:absolute;left:226px;top:196px;width:40px;height:50px;border-right:1.2px solid #9c9c9c;border-bottom:1.2px solid #9c9c9c}
.faq{position:absolute;left:24px;top:279px;width:230px;font:400 4.6px/1.35 "Roboto Condensed",sans-serif;color:var(--ink-soft)}
.faq h4{font:700 5.3px "Montserrat",sans-serif;color:var(--ink);margin-top:5px}
.faq h4:first-child{margin-top:0}
.faq-bracket{position:absolute;left:16px;top:275px;width:8px;height:92px;border:1.5px solid #8d8d8d;border-right:none}
.contact-mark{position:absolute;left:42px;top:380px;width:14px;height:14px;border-radius:50%;background:var(--pink)}
.contact-line{position:absolute;left:61px;top:381px;font:500 5.5px "Oswald",sans-serif;color:var(--ink)}
.contact-web{position:absolute;left:160px;top:396px;font:700 4.8px "Roboto Condensed",sans-serif;color:var(--pink)}
.contact-slash{position:absolute;left:228px;top:394px;width:26px;height:9px;background:var(--pink);clip-path:polygon(0 0,65% 0,100% 100%,35% 100%)}

/* outside: front cover */
.cover{position:absolute;left:280px;top:0;width:280px;height:431px;background:var(--paper)}
.cover-frame{position:absolute;left:8px;top:8px;right:8px;bottom:14px;border:0.6px solid #c9c8c4}
.brand{position:absolute;left:96px;top:50px;display:flex;align-items:center;gap:6px}
.brand-dot{width:17px;height:17px;border-radius:50%;background:var(--pink)}
.brand-name{font:400 13px "Oswald",sans-serif;color:var(--pink);letter-spacing:-.2px}
.brand-bracket{position:absolute;left:190px;top:30px;width:60px;height:60px;border-top:1.2px solid #9c9c9c;border-right:1.2px solid #9c9c9c}
.cover-diag{position:absolute;left:30px;top:36px;width:190px;height:300px;background:linear-gradient(to bottom right,transparent 49.6%,#cfcdc9 49.6%,#cfcdc9 50.4%,transparent 50.4%)}
.crowd-photo{position:absolute;left:112px;top:126px;width:168px;height:127px;
  background:radial-gradient(ellipse at 80% 10%,#f5e7c6,transparent 40%),linear-gradient(170deg,#5a4034,#7e3b3e 50%,#2b1b1b);
  clip-path:polygon(18% 0,100% 0,100% 100%,55% 100%)}
.crowd-stripe{position:absolute;left:112px;top:126px;width:168px;height:127px;background:var(--pink);clip-path:polygon(0 0,18% 0,55% 100%,40% 100%)}
.award{position:absolute;left:56px;top:128px;width:26px;height:26px;border-radius:50%;border:2px solid var(--gold);background:rgba(217,169,58,.15)}
.headline{position:absolute;left:19px;top:152px;font:500 17.5px/1.45 "Oswald",sans-serif;color:var(--navy);text-transform:uppercase}
.headline-rule{position:absolute;left:18px;top:255px;width:150px;height:0.8px;background:#b9b8b4}
.cover-copy{position:absolute;left:19px;top:264px;width:170px;font:italic 300 7.3px/1.9 "Montserrat",sans-serif;color:var(--ink-soft)}
.partner{position:absolute;left:210px;top:282px;font:400 5px "Montserrat",sans-serif;color:var(--navy);letter-spacing:.3px;text-align:center;width:60px}
.partner::before{content:"";display:block;width:16px;height:10px;margin:0 auto 3px;background:var(--navy)}
.cover-web{position:absolute;right:14px;bottom:14px;font:700 4.3px "Roboto Condensed",sans-serif;color:var(--pink)}
</style>
</head>
<body>
<main class="canvas">

  <!-- Inside spread -->
  <section class="spread spread--inside" aria-label="Brochure inside spread">
    <div class="fold-shade"></div>
    <div class="frame-line" style="left:12px;top:10px;right:10px;bottom:10px"></div>

    <header class="about-band">
      <h2 class="about-title">ABOUT MAYA LINDEN</h2>
      <p class="about-copy about-copy--a">Maya Linden is a best-selling author and one of the UK's foremost experts on relationships. A playful, vivacious and inspirational facilitator and relationship specialist committed to guiding individuals through their journey of self-discovery back to love &amp; peace after painful relationships &amp; events. She is the founder of Heartward Circle: the UK's #1 relationship seminar for women, a programme that has changed the lives of thousands of women since 2016. Maya has dedicated the past 10 years to helping women</p>
      <p class="about-copy about-copy--b">discover how extraordinary they are, to know their power and to understand how to be in their relationships with others and, most importantly, with themselves after loss or breakups. She has been showing women how to reconnect with their own journey again, whether married, single or separated, gifting this to women throughout the world.</p>
      <div class="founder-stripe"></div>
      <div class="founder-photo" role="img" aria-label="Portrait photo of the founder smiling"></div>
    </header>

    <div class="team-slash"></div>
    <h2 class="team-title">MEET THE REST OF THE TEAM</h2>
    <div class="fold-slash"></div>

    <div class="portrait tone-a" style="left:17px;top:122px" role="img" aria-label="Portrait photo of Nora Callan"></div>
    <div class="quote" style="left:96px;top:128px">
      <p class="quote-name">NORA CALLAN, 34,</p>
      <p class="quote-role">Missing and exploitation coordinator</p>
      <p class="quote-body">I joined Heartward Circle to solve issues I had in my relationships with men that I had been carrying for a long time. As a result of this work I can see things from a different perspective. The conversation that once dominated my mind about relationships is no longer there, no longer holding me back. I feel free now. This has been a life changing experience of which I am eternally grateful.</p>
    </div>

    <div class="quote quote--right" style="left:16px;top:218px">
      <p class="quote-name">ALICE HART, 63,</p>
      <p class="quote-role">Midwife labour ward</p>
      <p class="quote-body">"I honestly didn't know how this was going to help me get through the pain of my marriage breakup. Then one evening something in the message landed. Maya was talking about recognising and letting the emotions burn through, and that absolutely resonated with me. I continued with the classes in the hope of finding a way out of this pain. I began applying the tools being taught, which really helped give me space and time in the day to find me. A few weeks after, I started to see a real shift in me. I started to feel a sense of peace and I was able to manage these huge emotions. I've loved every minute of it."</p>
    </div>
    <div class="portrait tone-b" style="left:201px;top:224px" role="img" aria-label="Portrait photo of Alice Hart"></div>

    <div class="portrait tone-c" style="left:25px;top:326px" role="img" aria-label="Portrait photo of Alexa Sommer"></div>
    <div class="quote" style="left:103px;top:332px">
      <p class="quote-name">ALEXA SOMMER, 39,</p>
      <p class="quote-role">Receptionist for adult mental health</p>
      <p class="quote-body">I feel incredibly lucky to have found this group of amazing women. The sessions and network have opened my eyes to how I treat myself, my thoughts, my emotions, and my mindset in general. The sessions have gifted me in-depth information and tools to put in place to break my trauma &amp; addiction cycles. I have learnt to give myself more compassion &amp; self-love.</p>
    </div>

    <div class="quote quote--right" style="left:297px;top:122px">
      <p class="quote-name">CLARA, 42,</p>
      <p class="quote-role">Hairstylist</p>
      <p class="quote-body">The sessions have been a fantastic way of consolidating Maya's teaching in my mind after the weekends. It has been a great way to keep consistency in the tools, which are disciplines that I very much need to shift my mindset. Through the questions and answers I can see practical ways in which others are applying the teaching. I gain insights into my own habits and unhelpful thinking, and I appreciate the courage and insight of the other circle members.</p>
    </div>
    <div class="portrait tone-d" style="left:476px;top:118px" role="img" aria-label="Portrait photo of Clara"></div>

    <div class="portrait tone-e" style="left:293px;top:228px" role="img" aria-label="Portrait photo of Mel Granger"></div>
    <div class="quote" style="left:372px;top:234px">
      <p class="quote-name">MEL GRANGER, 33,</p>
      <p class="quote-role">Senior customer success manager</p>
      <p class="quote-body">The sessions are like mini mastery weekends, absolutely life changing. I've finally realised why I keep reliving patterns of behaviour like comparison, feeling worthless or stupid, and it's because I haven't dealt with deep down emotions that I learnt to suppress as a child. I now have the tools to see these emotions as they come up and process them instead of ignoring them. I'm finally ready to love and accept myself for who I am.</p>
    </div>

    <div class="quote quote--right" style="left:296px;top:330px">
      <p class="quote-name">MARISOL REYES, 38,</p>
      <p class="quote-role">Director of luxury sales</p>
      <p class="quote-body">The session series is my most important weekly date with myself! They involve a deeper learning of all the tools. Having the chance to go through each of them in detail allows me to engage in the benefit of practising them each day. It is so powerful to learn about the senior members and their journeys and how they have used the tools to become safer within themselves.</p>
    </div>
    <div class="portrait tone-f" style="left:474px;top:312px" role="img" aria-label="Portrait photo of Marisol Reyes"></div>

    <div class="foot-stripes" style="left:-4px">
      <span style="width:26px;background:#7b7b7b"></span>
      <span style="width:120px;background:var(--blue)"></span>
      <span style="width:22px;background:var(--pink)"></span>
    </div>
  </section>

  <!-- Outside spread -->
  <section class="spread spread--outside" aria-label="Brochure outside spread">
    <!-- back cover -->
    <p class="kicker">DON'T LET TODAY FINISH HERE!</p>
    <div class="stage-stripe"></div>
    <div class="stage-photo" role="img" aria-label="Photo of the founder speaking on stage in a blue dress"></div>
    <div class="register-band">Register today and get the first<br>months' worth TODAY.</div>

    <p class="sub-label">SUBSCRIPTION:</p>
    <p class="sub-price">£200 A MONTH</p>
    <p class="sub-copy">Tomorrow, wake up and watch half a day of the most powerful content for relationships out there.<br><b>That's half a day of advanced content for only £200.</b></p>
    <p class="sub-note">If at any point you wish to cancel your subscription, just give us 30 days notice.</p>

    <div class="detail" style="top:191px">
      <h4>About The Sessions:</h4>
      Immerse yourself for one hour a week with like-minded individuals from the comfort and safety of your own home.
    </div>
    <div class="detail" style="top:226px;width:160px">
      <h4>What's Included:</h4>
      1. Receive full access to the Connection Growth Programme (once a week)<br>
      2. Gain full access to the network via our private members forum.
    </div>
    <div class="pink-block"></div>
    <div class="schedule-bracket"></div>
    <p class="schedule">MONDAYS<span>7PM-8PM</span></p>

    <div class="faq-bracket"></div>
    <div class="faq">
      <h4>Is this programme for me?</h4>
      <p>If you wish to join one of the UK's top female networks for a life changing year but the full programme is out of budget, then the Connection Growth Programme is for you. Give yourself that step in between. We've packaged it up so that you can afford it!</p>
      <h4>What will I learn/get from the programme?</h4>
      <p>• Weekly opportunity to have all your burning relationship questions answered<br>
      • Immerse with a powerful network of like-minded women and learn even more<br>
      • Tools to help you overcome past relationship wounds and patterns<br>
      • Deepen your understanding of self-mastery on route to relationship mastery</p>
    </div>

    <div class="contact-mark"></div>
    <p class="contact-line">CONTACT@HEARTWARDCIRCLE-EXAMPLE.COM | +44 20 0000 0142</p>
    <p class="contact-web">heartwardcircle-example.com</p>
    <div class="contact-slash"></div>

    <!-- front cover -->
    <div class="cover">
      <div class="cover-frame"></div>
      <div class="cover-diag"></div>
      <div class="brand-bracket"></div>
      <div class="brand"><span class="brand-dot"></span><span class="brand-name">HEARTWARD CIRCLE</span></div>
      <div class="crowd-stripe"></div>
      <div class="crowd-photo" role="img" aria-label="Photo of a large seminar audience of women in a theatre"></div>
      <div class="award" role="img" aria-label="Number one award badge"></div>
      <h1 class="headline">UK's<br>Relationship<br>Seminar for<br>Women only</h1>
      <div class="headline-rule"></div>
      <p class="cover-copy">Immerse yourself with a group of likeminded individuals in a weekly session and get absorbed in some of the most senior relationships content that's changing the lives of thousands of women internationally.</p>
      <p class="partner">LUMEN SESSIONS</p>
      <div class="foot-stripes" style="left:8px;bottom:10px">
        <span style="width:30px;background:#7b7b7b"></span>
        <span style="width:130px;background:var(--blue)"></span>
        <span style="width:14px;background:var(--pink)"></span>
        <span style="width:6px;background:var(--blue)"></span>
      </div>
      <p class="cover-web">heartwardcircle-example.com</p>
    </div>
  </section>

</main>
</body>
</html>
```